Desktop and Networking Support Course 9.17.25

Important the ad should not be very busy with the text taking up the major part of the ad .. please do not make the text so big that it takes up most of the ad..
Flyer Design Brief for Graphic Artist
also i am looking for something unique or creative that it will stand out .
Size & Layout:
Full Page with Bleed: 8” x 10.75” + 0.25” bleed on all sides.
Footer Space: Leave a 1-inch margin at the bottom for footer content (e.g., contact info, logo, or call-to-action).
Target Audience:
College-age students (around 24 years old)
Located in the USA
Interested in creative, professional, and career-building opportunities
Purpose:
To attract students to enroll in a college program
Flyer should be eye-catching, unique, and creative
Text must be clear and readable,
Design Style:
Use vector art, typography, or photography — your choice
If using photography, feature a white young professional USA citizen:
Wearing a white collared shirt
not with long hair
Creative Direction:
The flyer should stand out visually — something people would want to look at and keep
Showcase creativity and professionalism
Use bold colors, dynamic layout, or unexpected design elements to grab attention
Avoid clutter — keep the design balanced and clean
Text Suggestions (can be adjusted):
Footer,
please leave one inch on the bottom for the footer

```html
<!DOCTYPE html>
<html lang="en">
<head>
<meta charset="UTF-8">
<title>Desktop &amp; Network Support Course</title>
<link href="https://fonts.googleapis.com/css2?family=Poppins:ital,wght@0,500;0,700;0,800;1,300;1,400&family=Inter:wght@400;700&display=swap" rel="stylesheet">
<style>
  :root {
    --brand-blue: #0c4db6;
    --brand-blue-deep: #0a3f9c;
    --accent-yellow: #ffc300;
    --ink: #111111;
    --ink-soft: #1e1e1e;
    --paper: #ffffff;
    --shirt-light: #eeeeec;
    --shirt-shade: #cfcfcb;
  }
  * { margin: 0; padding: 0; box-sizing: border-box; }
  html, body { width: 927px; height: 1200px; overflow: hidden; background: var(--paper); }
  .flyer {
    position: relative;
    width: 927px;
    height: 1200px;
    overflow: hidden;
    background: var(--paper);
    font-family: "Poppins", sans-serif;
  }
  .backdrop { position: absolute; inset: 0; }
  .footer-band {
    position: absolute;
    left: 0; right: 0; bottom: 0;
    height: 112px;
    background: var(--accent-yellow);
  }
  .portrait {
    position: absolute;
    left: 546px;
    top: 315px;
    width: 364px;
    height: 885px;
    border-radius: 150px 150px 20px 20px;
    background: linear-gradient(180deg, #c99a7c 0%, #d8ae92 22%, var(--shirt-light) 34%, var(--shirt-shade) 70%, #4a4a48 86%, #3a3a38 100%);
  }
  .headline {
    position: absolute;
    left: 74px; top: 58px;
    color: var(--accent-yellow);
    font-weight: 800;
    font-size: 55px;
    line-height: 54px;
    letter-spacing: -0.5px;
    white-space: nowrap;
  }
  .course-title {
    position: absolute;
    left: 74px; top: 190px;
    color: var(--paper);
    font-weight: 700;
    font-size: 36px;
    line-height: 44px;
    white-space: nowrap;
  }
  .course-focus {
    position: absolute;
    left: 74px; top: 279px;
    color: var(--paper);
    font-weight: 700;
    font-size: 27px;
    line-height: 37px;
    white-space: nowrap;
  }
  .course-stat {
    position: absolute;
    left: 74px; top: 352px;
    color: var(--paper);
    font-style: italic;
    font-weight: 300;
    font-size: 21px;
    letter-spacing: 0.3px;
    white-space: nowrap;
  }
  .training-title {
    position: absolute;
    left: 45px; top: 708px;
    color: var(--brand-blue);
    font-weight: 700;
    font-size: 31.5px;
    line-height: 44px;
    white-space: nowrap;
  }
  .training-points {
    position: absolute;
    left: 45px; top: 807px;
    color: var(--ink-soft);
    font-style: italic;
    font-size: 21px;
    line-height: 35px;
    white-space: nowrap;
  }
  .ranking {
    position: absolute;
    left: 45px; top: 900px;
    color: var(--ink-soft);
    font-style: italic;
    font-size: 24px;
    line-height: 33px;
    white-space: nowrap;
  }
  .benefits {
    position: absolute;
    left: 58px; top: 1007px;
    list-style: none;
    color: var(--ink);
    font-weight: 800;
    font-size: 21px;
    line-height: 30px;
    white-space: nowrap;
  }
  .benefits li { position: relative; padding-left: 23px; }
  .benefits li::before {
    content: "";
    position: absolute;
    left: 0; top: 12px;
    width: 7px; height: 7px;
    border-radius: 50%;
    background: var(--ink);
  }
  .website {
    position: absolute;
    left: 45px; top: 1120px;
    display: flex;
    align-items: center;
    gap: 19px;
    font-family: "Inter", sans-serif;
    color: var(--brand-blue-deep);
  }
  .website-icon { width: 48px; height: 48px; }
  .website-label { font-size: 21px; line-height: 24px; }
  .website-url { font-size: 21px; font-weight: 700; line-height: 24px; }
</style>
</head>
<body>
  <main class="flyer">
    <svg class="backdrop" width="927" height="1200" viewBox="0 0 927 1200">
      <defs>
        <linearGradient id="skylineTone" x1="0" y1="0" x2="1" y2="1">
          <stop offset="0" stop-color="#2a64c0"/>
          <stop offset="0.5" stop-color="#0f4fb6"/>
          <stop offset="1" stop-color="#3a7ad0"/>
        </linearGradient>
      </defs>
      <path class="accent-swoosh" d="M0,375 C330,680 760,710 927,650 V732 C760,760 320,760 0,415 Z" fill="#ffc300"/>
      <path class="skyline-panel" role="img" aria-label="Blue-toned city skyline photograph with halftone dots" d="M0,0 H927 V650 C760,710 330,680 0,375 Z" fill="url(#skylineTone)"/>
    </svg>

    <div class="footer-band"></div>

    <div class="portrait" role="img" aria-label="Photo of a smiling young professional in a white collared shirt and red striped tie"></div>

    <h1 class="headline">YOUR CAREER IS JUST A<br>CLICK AWAY</h1>
    <h2 class="course-title">DESKTOP &amp; NETWORK SUPPORT COURSE</h2>
    <p class="course-focus">MASTER VANTIX<br>OPERATING SYSTEMS</p>
    <p class="course-stat">90% EMPLOYMENT RATE – CLASS OF 2024</p>

    <h3 class="training-title">HANDS-ON DESKTOP &amp;<br>NETWORK TRAINING</h3>
    <p class="training-points">REAL-WORLD TROUBLESHOOTING SKILLS<br>READY FOR IT JOBS</p>
    <p class="ranking">PREPARE FOR 3 OF THE TOP 10 TECH JOBS<br>NATIONAL CAREER DIGEST 2025</p>

    <ul class="benefits">
      <li>IN-PERSON AND REMOTE OPTIONS</li>
      <li>PARTIAL SCHOLARSHIPS OFFERED</li>
    </ul>

    <div class="website">
      <svg class="website-icon" viewBox="0 0 48 48" aria-hidden="true">
        <circle cx="24" cy="24" r="24" fill="#0c4db6"/>
        <g fill="none" stroke="#ffc300" stroke-width="2.2">
          <circle cx="24" cy="24" r="13"/>
          <ellipse cx="24" cy="24" rx="6" ry="13"/>
          <line x1="11" y1="24" x2="37" y2="24"/>
          <line x1="24" y1="11" x2="24" y2="37"/>
          <path d="M13.5,17 H34.5 M13.5,31 H34.5"/>
        </g>
      </svg>
      <div>
        <div class="website-label">Visit Our Website:</div>
        <div class="website-url">www.website.com</div>
      </div>
    </div>
  </main>
</body>
</html>
```